Flyer für Reifen- und Autoservicebetrieb
Zielgruppe
Wir sind ein Reifen- und Autoservicebetrieb; eine freie KFZ-Meister-Werkstatt ohne Markenbindung.
Aufgabenstellung
Im Focus des Flyers soll auf der Vorderseite der Reifenservice stehen, da dieser zur bevorstehenden Winterreifen-Wechselsaison erscheinen wird (Reifenwechsel, Einlagerung, Räderwäsche, Online-Termin). Auf der Rückseite soll der Autoservice und der 'neu' angebotene LKW- und Landwirtschafts- Reifenservice beworben werden.

```html
<!DOCTYPE html>
<html lang="de">
<head>
<meta charset="utf-8">
<title>Korvana Reifen – Flyer Reifenservice und KFZ-Service</title>
<link href="https://fonts.googleapis.com/css2?family=Bebas+Neue&family=Montserrat:wght@800&family=Questrial&display=swap" rel="stylesheet">
<style>
  :root {
    --orange: #f08c00;
    --slate: #80999c;
    --ink: #2e3c43;
    --list: #3d4a50;
    --body: #4b555a;
    --paper: #ffffff;
    --paper-shade: #e5e7e8;
    --stage: #767676;
  }
  * { box-sizing: border-box; margin: 0; padding: 0; }
  html, body { width: 1200px; height: 1117px; overflow: hidden; }
  body { background: var(--stage); position: relative; }

  .flyer {
    position: absolute; top: 177px; width: 534px; height: 763px; overflow: hidden;
    background: linear-gradient(180deg, var(--paper) 0%, #f1f2f2 60%, var(--paper-shade) 100%);
  }
  .flyer--front { left: 58px; }
  .flyer--back { left: 608px; }

  .photo {
    position: absolute; left: 232px; top: 16px; width: 302px; height: 252px;
    clip-path: polygon(48px 0, 100% 0, 100% 100%, 0 100%);
  }
  .photo--tyre { background: linear-gradient(135deg, #5c5a58 0%, #2a2a2c 45%, #1b1c1e 70%, #3b6f97 100%); }
  .photo--workshop { background: linear-gradient(135deg, #6f8fa8 0%, #c9d3da 40%, #23324d 65%, #e6ebee 100%); }

  .shapes { position: absolute; inset: 0; width: 534px; height: 763px; }

  .brand {
    position: absolute; left: 45px; top: 48px; display: flex; align-items: center; gap: 10px;
    font-family: "Montserrat", sans-serif; font-weight: 800; font-size: 22px;
    color: var(--orange); letter-spacing: 0.5px; text-transform: uppercase;
  }
  .brand-dot { width: 34px; height: 34px; border-radius: 50%; background: var(--slate); }

  .headline {
    position: absolute; left: 46px; top: 125px;
    font-family: "Bebas Neue", sans-serif; font-size: 42px; line-height: 39px; color: #fff;
  }

  .section-title {
    position: absolute; left: 0; width: 534px; text-align: center;
    font-family: "Bebas Neue", sans-serif; color: #fff; line-height: 1;
  }
  .section-title--tyre { top: 300px; font-size: 56px; }
  .section-title--car { top: 308px; font-size: 62px; }
  .section-sub {
    position: absolute; left: 0; top: 352px; width: 534px; text-align: center;
    font-family: "Bebas Neue", sans-serif; font-size: 18px; color: #fff;
  }

  .intro {
    position: absolute; left: 40px; width: 454px; text-align: center;
    font-family: "Questrial", sans-serif; font-size: 13.5px; line-height: 18.7px; color: var(--body);
  }
  .intro--tyre { top: 397px; }
  .intro--car { top: 398px; width: 480px; left: 27px; }

  .services { position: absolute; list-style: none; }
  .services li {
    position: relative; font-family: "Montserrat", sans-serif; font-weight: 800;
    font-size: 12.6px; line-height: 17px; color: var(--list); margin-bottom: 6px;
  }
  .services li::before {
    content: ""; position: absolute; left: -22px; top: 4px; width: 8px; height: 9px;
    background: var(--orange); clip-path: polygon(0 0, 100% 50%, 0 100%);
  }
  .services--front-a { left: 71px; top: 457px; }
  .services--front-b { left: 293px; top: 457px; }
  .services--back-a { left: 74px; top: 439px; }
  .services--back-a li:last-child { line-height: 15px; }
  .services--back-b { left: 315px; top: 439px; }
  .services--back-b li { margin-bottom: 9px; }

  .offer {
    position: absolute; left: 0; top: 606px; width: 534px; text-align: center;
    font-family: "Bebas Neue", sans-serif; font-size: 21.5px; line-height: 24px; color: var(--orange);
  }

  .phone-icon { position: absolute; left: 45px; top: 659px; width: 54px; height: 54px; }
  .phone-number {
    position: absolute; left: 113px; top: 656px;
    font-family: "Bebas Neue", sans-serif; font-size: 71px; line-height: 1; color: var(--ink); letter-spacing: 0.5px;
  }

  .contact {
    position: absolute; top: 729px; display: flex; align-items: center; gap: 9px;
    font-family: "Questrial", sans-serif; font-size: 16px; font-weight: 700; color: #fff;
  }
  .contact svg { width: 17px; height: 17px; }
  .contact--mail { left: 58px; }
  .contact--web { left: 286px; }
</style>
</head>
<body>

<!-- Vorderseite: Reifenservice -->
<section class="flyer flyer--front">
  <div class="photo photo--tyre" role="img" aria-label="Foto: Mechaniker montiert mit Schlagschrauber ein Rad an einem Fahrzeug auf der Hebebühne"></div>

  <svg class="shapes" viewBox="0 0 534 763" aria-hidden="true">
    <polygon points="377,266 387,255 534,255 534,378 68,378 58,397 0,397 0,266" fill="var(--slate)"/>
    <polygon points="64,374 484,374 481,380 61,380" fill="var(--orange)"/>
    <polygon points="33,113 286,113 226,291 0,291 0,210" fill="var(--orange)"/>
    <polygon points="0,457 11,465 11,577 0,585" fill="var(--orange)"/>
    <polygon points="534,457 523,465 523,577 534,585" fill="var(--orange)"/>
    <polygon points="90,599 440,599 452,623 78,623" fill="var(--paper-shade)"/>
    <rect x="0" y="623" width="534" height="140" fill="var(--paper-shade)"/>
    <rect x="0" y="736" width="534" height="27" fill="var(--slate)"/>
    <polygon points="39,719 494,719 508,763 24,763" fill="var(--orange)"/>
  </svg>

  <div class="brand"><span class="brand-dot"></span>Korvana Reifen</div>

  <h1 class="headline">Reifen und<br>Autoservice<br>für Ihr<br>Fahrzeug</h1>

  <h2 class="section-title section-title--tyre">Unser Reifenservice</h2>
  <p class="section-sub">Wartung und Pflege für Ihre Räder und Reifen</p>

  <p class="intro intro--tyre">Unsere hochwertigen Reifen und Services sorgen<br>für Sicherheit, Langlebigkeit und eine optimale Leistung<br>Ihrer Räder und Reifen.</p>

  <ul class="services services--front-a">
    <li>WINTERREIFEN</li>
    <li>RÄDEREINLAGERUNG</li>
    <li>REIFENMONTAGE</li>
    <li>AUSWUCHTEN</li>
    <li>REIFENCHECK</li>
    <li>REIFENREPARATUR</li>
  </ul>
  <ul class="services services--front-b">
    <li>LUFTDRUCKKONTROLLE</li>
    <li>KALIBRIERUNG DES REIFEN-<br>DRUCKKONTROLLSYSTEMS</li>
    <li>RÄDERWÄSCHE</li>
    <li>SAISONALER RÄDER /<br>REIFENWECHSEL</li>
  </ul>

  <p class="offer">Erleben Sie unsere hochwertigen<br>Reifen- und Service-Angebote für Ihr Auto</p>

  <svg class="phone-icon" viewBox="0 0 24 24" aria-hidden="true">
    <path fill="var(--orange)" d="M6.6 2.2c.5-.3 1.1-.2 1.5.3l2.4 3.3c.4.5.3 1.2-.1 1.6L8.8 8.9c.9 2.4 3.4 5 6.3 6.3l1.5-1.6c.4-.4 1.1-.5 1.6-.1l3.3 2.4c.5.4.6 1 .3 1.5l-1.4 2.5c-.5.9-1.6 1.4-2.6 1.1C10.7 19.2 4.8 13.3 3 6.2c-.3-1 .2-2.1 1.1-2.6z"/>
  </svg>
  <p class="phone-number">04123 567 89 10</p>

  <p class="contact contact--mail">
    <svg viewBox="0 0 20 20" aria-hidden="true"><circle cx="10" cy="10" r="9" fill="none" stroke="#fff" stroke-width="1.6"/><rect x="5" y="6.5" width="10" height="7" fill="none" stroke="#fff" stroke-width="1.4"/><path d="M5 7l5 4 5-4" fill="none" stroke="#fff" stroke-width="1.4"/></svg>
    info@korvana-reifen.de
  </p>
  <p class="contact contact--web">
    <svg viewBox="0 0 20 20" aria-hidden="true"><circle cx="10" cy="10" r="8.5" fill="none" stroke="#fff" stroke-width="1.6"/><ellipse cx="10" cy="10" rx="3.8" ry="8.5" fill="none" stroke="#fff" stroke-width="1.3"/><path d="M1.5 10h17M3 6h14M3 14h14" stroke="#fff" stroke-width="1.2"/></svg>
    www.korvana-reifen.de
  </p>
</section>

<!-- Rückseite: KFZ-Service -->
<section class="flyer flyer--back">
  <div class="photo photo--workshop" role="img" aria-label="Foto: Mechaniker mit Diagnosegerät vor geöffneter Motorhaube in einer Werkstatthalle"></div>

  <svg class="shapes" viewBox="0 0 534 763" aria-hidden="true">
    <polygon points="377,266 387,255 534,255 534,378 68,378 58,397 0,397 0,266" fill="var(--slate)"/>
    <polygon points="64,374 484,374 481,380 61,380" fill="var(--orange)"/>
    <polygon points="33,113 286,113 226,291 0,291 0,210" fill="var(--orange)"/>
    <polygon points="0,457 11,465 11,577 0,585" fill="var(--orange)"/>
    <polygon points="534,457 523,465 523,577 534,585" fill="var(--orange)"/>
    <polygon points="90,599 440,599 452,623 78,623" fill="var(--paper-shade)"/>
    <rect x="0" y="623" width="534" height="140" fill="var(--paper-shade)"/>
    <rect x="0" y="736" width="534" height="27" fill="var(--slate)"/>
    <polygon points="39,719 494,719 508,763 24,763" fill="var(--orange)"/>
  </svg>

  <div class="brand"><span class="brand-dot"></span>Korvana Reifen</div>

  <h1 class="headline">Reifen und<br>Autoservice<br>für Ihr<br>Fahrzeug</h1>

  <h2 class="section-title section-title--car">Unser KFZ-Service</h2>

  <p class="intro intro--car">Unsere Meisterwerkstatt punktet nicht nur mit modernster<br>Ausstattung, sondern auch mit kompetenten Mitarbeitern.</p>

  <ul class="services services--back-a">
    <li>INSPEKTION</li>
    <li>ÖLSERVICE</li>
    <li>KLIMASERVICE</li>
    <li>FEHLERDIAGNOSE</li>
    <li>STOSSDÄMPFER-SERVICE</li>
    <li>HAUPTUNTERSUCHUNG/<br>ABGASUNTERSUCHUNG (HU/AU)</li>
  </ul>
  <ul class="services services--back-b">
    <li>BREMSENSERVICE</li>
    <li>WINTERCHECK</li>
    <li>BATTERIESERVICE</li>
    <li>FAHRZEUGREPARATUR<br>SERVICE</li>
  </ul>

  <p class="offer">Erleben Sie unsere hochwertigen<br>Reifen- und Service-Angebote für Ihr Auto</p>

  <svg class="phone-icon" viewBox="0 0 24 24" aria-hidden="true">
    <path fill="var(--orange)" d="M6.6 2.2c.5-.3 1.1-.2 1.5.3l2.4 3.3c.4.5.3 1.2-.1 1.6L8.8 8.9c.9 2.4 3.4 5 6.3 6.3l1.5-1.6c.4-.4 1.1-.5 1.6-.1l3.3 2.4c.5.4.6 1 .3 1.5l-1.4 2.5c-.5.9-1.6 1.4-2.6 1.1C10.7 19.2 4.8 13.3 3 6.2c-.3-1 .2-2.1 1.1-2.6z"/>
  </svg>
  <p class="phone-number">04123 567 89 10</p>

  <p class="contact contact--mail">
    <svg viewBox="0 0 20 20" aria-hidden="true"><circle cx="10" cy="10" r="9" fill="none" stroke="#fff" stroke-width="1.6"/><rect x="5" y="6.5" width="10" height="7" fill="none" stroke="#fff" stroke-width="1.4"/><path d="M5 7l5 4 5-4" fill="none" stroke="#fff" stroke-width="1.4"/></svg>
    info@korvana-reifen.de
  </p>
  <p class="contact contact--web">
    <svg viewBox="0 0 20 20" aria-hidden="true"><circle cx="10" cy="10" r="8.5" fill="none" stroke="#fff" stroke-width="1.6"/><ellipse cx="10" cy="10" rx="3.8" ry="8.5" fill="none" stroke="#fff" stroke-width="1.3"/><path d="M1.5 10h17M3 6h14M3 14h14" stroke="#fff" stroke-width="1.2"/></svg>
    www.korvana-reifen.de
  </p>
</section>

</body>
</html>
```